Young Architect Bussiness Card

English is not my first language (spanish is).
Need a bussiness card design for my best friend who is about to graduate from college, Licentiate degree in architecture, so she needs business cards to start networking, currently she has no porfolio, web page or facebook. so she is relying on her cel phone and gmail, but should leave space for one of them (facebook)

Design for business card should be modern, maybe something with construction blue prints patern or 3D modelling.

Name: Mariela Fonseca Arrieta
Licentiate in Arquitecture
Cel: (506) XXX-4827
email: marielaXXX@correovela.com

Services, although im not sure if it has to be there or not:
Anteproyectos / Proposal design
Inspecciones / Site Inspections
Modelado 3D / 3D modelling
Planos Constructivos / Construction Blue Prints
Presupuestos / Budgets

Design should be in spanish

Contact Information for Business Card

Name: Mariela Fonseca, Arquitecto
Associtation code : XXXX
Phone: (506) XXXX-XXXX
Email: xxx@correovela.com
Facebook: xxxx

Requirements
Must have
• Design for business card should be modern, maybe something with construction blue prints patern or 3D modelling.
Nice to have
• Something like a transition from 2D to 3D.

```html
<!DOCTYPE html>
<html lang="es">
<head>
<meta charset="utf-8">
<title>Tarjeta de presentación – Mariela Fonseca, Arquitecta</title>
<link rel="stylesheet" href="https://fonts.googleapis.com/css2?family=Noto+Sans:wght@400;700&display=swap">
<style>
  :root {
    --page-bg: #e9e9e9;
    --card-bg: #f4f4f4;
    --ink: #2b2b2b;
    --accent-purple: #9e65a2;
    --accent-green: #6ab962;
    --accent-teal: #00adbb;
    --white: #ffffff;
  }
  html, body {
    margin: 0;
    padding: 0;
    width: 1200px;
    height: 1200px;
    overflow: hidden;
    background: var(--page-bg);
    font-family: "Noto Sans", Verdana, sans-serif;
  }
  .canvas {
    position: relative;
    width: 1200px;
    height: 1200px;
  }
  .card {
    position: absolute;
    left: 240px;
    width: 718px;
    height: 434px;
    background: var(--card-bg);
    box-shadow: 0 10px 18px rgba(0,0,0,0.12);
    overflow: hidden;
  }
  .card--front { top: 106px; }
  .card--back  { top: 600px; }

  /* Brand mark */
  .brand {
    position: absolute;
    display: flex;
    align-items: center;
    color: var(--ink);
    font-weight: 700;
    white-space: nowrap;
    line-height: 1;
  }
  .brand__square {
    display: block;
    background: var(--ink);
  }
  .card--front .brand {
    left: 96px;
    top: 140px;
    font-size: 22px;
    gap: 10px;
  }
  .card--front .brand__square { width: 18px; height: 18px; }
  .card--back .brand {
    left: 0;
    right: 0;
    top: 142px;
    justify-content: center;
    font-size: 54px;
    gap: 22px;
  }
  .card--back .brand__square { width: 40px; height: 40px; }

  /* Identity */
  .identity {
    position: absolute;
    left: 318px;
    top: 134px;
    width: 320px;
    text-align: center;
  }
  .identity__name {
    margin: 0;
    font-size: 28px;
    font-weight: 700;
    color: var(--ink);
    letter-spacing: 0.5px;
    line-height: 1.1;
  }
  .identity__role {
    margin: 2px 0 0;
    font-size: 16px;
    font-weight: 400;
    color: var(--accent-teal);
    letter-spacing: 2px;
    line-height: 1.2;
  }

  /* Contact band */
  .contact-band {
    position: absolute;
    left: 0;
    bottom: 0;
    width: 100%;
    height: 122px;
    display: flex;
  }
  .contact-band__item {
    flex: 1;
    display: flex;
    flex-direction: column;
    align-items: center;
    padding-top: 24px;
    color: var(--white);
    font-size: 14px;
    font-weight: 700;
    letter-spacing: 0.4px;
    white-space: nowrap;
  }
  .contact-band__item svg { display: block; margin-bottom: 12px; }
  .contact-band__item--phone { background: var(--accent-purple); }
  .contact-band__item--mail  { background: var(--accent-green); }
  .contact-band__item--code  { background: var(--accent-teal); }

  /* Back footer stripe */
  .footer-stripe {
    position: absolute;
    left: 0;
    bottom: 0;
    width: 100%;
    height: 12px;
    display: flex;
  }
  .footer-stripe span { flex: 1; }
  .stripe--purple { background: var(--accent-purple); }
  .stripe--green  { background: var(--accent-green); }
  .stripe--teal   { background: var(--accent-teal); }
</style>
</head>
<body>
<main class="canvas">

  <section class="card card--front" aria-label="Frente de la tarjeta">
    <div class="brand"><span class="brand__square"></span>Casa Vela</div>

    <div class="identity">
      <h1 class="identity__name">Mariela Fonseca</h1>
      <p class="identity__role">ARQUITECTA</p>
    </div>

    <div class="contact-band">
      <div class="contact-band__item contact-band__item--phone">
        <svg width="32" height="32" viewBox="0 0 32 32" aria-hidden="true">
          <circle cx="16" cy="16" r="16" fill="#fff"/>
          <path d="M11.2 8.5c.6-.4 1.3-.3 1.7.3l1.6 2.4c.4.6.3 1.3-.2 1.8l-1 .9c.8 1.8 2.3 3.4 4.1 4.3l.9-1c.5-.5 1.2-.6 1.8-.2l2.4 1.6c.6.4.7 1.2.3 1.7l-1 1.4c-.6.8-1.7 1.1-2.7.8-4.6-1.5-8.1-5.1-9.5-9.7-.3-1 0-2.1.8-2.7z" fill="var(--accent-purple)"/>
        </svg>
        (506) XXX-4827
      </div>
      <div class="contact-band__item contact-band__item--mail">
        <svg width="32" height="32" viewBox="0 0 32 32" aria-hidden="true">
          <circle cx="16" cy="16" r="16" fill="#fff"/>
          <rect x="8.5" y="10.5" width="15" height="11" rx="1" fill="var(--accent-green)"/>
          <path d="M9 11.5l7 5.5 7-5.5" fill="none" stroke="#fff" stroke-width="1.4"/>
        </svg>
        XXX@CORREOVELA.COM
      </div>
      <div class="contact-band__item contact-band__item--code">
        <svg width="32" height="32" viewBox="0 0 32 32" aria-hidden="true">
          <circle cx="16" cy="16" r="16" fill="#fff"/>
          <path d="M10 16.5l4 4 8-9" fill="none" stroke="var(--accent-teal)" stroke-width="2.6" stroke-linecap="round" stroke-linejoin="round"/>
        </svg>
        CÓD. ASOCIACIÓN XXXX
      </div>
    </div>
  </section>

  <section class="card card--back" aria-label="Reverso de la tarjeta">
    <div class="brand"><span class="brand__square"></span>Casa Vela</div>
    <div class="footer-stripe">
      <span class="stripe--purple"></span>
      <span class="stripe--green"></span>
      <span class="stripe--teal"></span>
    </div>
  </section>

</main>
</body>
</html>
```